plumbing & gas fitting business card design

We need a business card design for a plumbing & gas fitting company. The company covers commercial, domestic and maintenance work. We would like a modern design communicating efficiency and sophistication. preferred colours would include (red grey & black) or (green grey & black). Please DO NOT include any water droplets.

Industry/Entity Type

Business

Contact Information for Business Card

Vortig Plumbing & Gas, Commercial Domestic & Maintenance, licence no. 617394K, ABN 47215830962, Phone 0417382956, Email vortigplumbingandgas@corvanet.com

```html
<!DOCTYPE html>
<html lang="en">
<head>
<meta charset="utf-8">
<title>Vortig Plumbing &amp; Gas – Business Card</title>
<link rel="stylesheet" href="https://fonts.googleapis.com/css2?family=Lato:wght@400;700;900&display=swap">
<style>
  :root {
    --stage: #e9e6e2;
    --card-dark: #1b1b1c;
    --card-mid: #2c2c2e;
    --card-light: #5a5a5c;
    --brand-red: #d6202f;
    --text-white: #ffffff;
    --text-soft: #d9d9d9;
    --rule: #8a8a8a;
  }
  * { box-sizing: border-box; margin: 0; padding: 0; }
  html, body { width: 1200px; height: 646px; overflow: hidden; }
  body {
    background: var(--stage);
    font-family: "Lato", Arial, sans-serif;
    display: flex;
    align-items: center;
    justify-content: center;
    gap: 48px;
  }
  .card {
    position: relative;
    width: 540px;
    height: 292px;
    overflow: hidden;
    color: var(--text-white);
    box-shadow: 0 10px 28px rgba(0,0,0,0.28);
  }
  .card--back {
    background: radial-gradient(ellipse 60% 70% at 50% 22%, var(--card-light) 0%, var(--card-mid) 45%, var(--card-dark) 100%);
  }
  .card--front {
    background: radial-gradient(ellipse 55% 75% at 18% 88%, var(--card-light) 0%, var(--card-mid) 45%, var(--card-dark) 100%);
  }
  .brand {
    position: absolute;
    display: flex;
    align-items: center;
  }
  .card--back .brand { left: 46px; top: 58px; }
  .card--front .brand { left: 46px; top: 40px; }
  .brand__dot {
    width: 58px;
    height: 58px;
    border-radius: 50%;
    background: var(--brand-red);
    border: 2px solid #f1f1f1;
    flex: none;
  }
  .brand__divider {
    width: 1px;
    height: 48px;
    background: var(--rule);
    margin: 0 20px 0 22px;
  }
  .brand__name {
    font-weight: 700;
    font-size: 19px;
    letter-spacing: 0.3px;
    color: var(--brand-red);
    text-transform: uppercase;
    line-height: 1.1;
  }
  .brand__tagline {
    font-weight: 700;
    font-size: 10.5px;
    color: var(--text-white);
    text-transform: uppercase;
    margin-top: 3px;
    letter-spacing: 0.2px;
  }
  .web-band {
    position: absolute;
    left: 0;
    right: 0;
    top: 196px;
    height: 40px;
    background: var(--brand-red);
    display: flex;
    align-items: center;
    padding-left: 46px;
  }
  .web-band__url {
    font-weight: 700;
    font-size: 16px;
    letter-spacing: 0.5px;
    text-transform: uppercase;
    color: var(--text-white);
  }
  .contact {
    position: absolute;
    left: 46px;
    bottom: 36px;
    display: flex;
    align-items: stretch;
  }
  .person { align-self: flex-end; margin-right: 16px; }
  .person__name {
    font-weight: 700;
    font-size: 13px;
    text-transform: uppercase;
  }
  .person__role {
    font-weight: 700;
    font-size: 10.5px;
    text-transform: uppercase;
    color: var(--text-soft);
    margin-top: 2px;
  }
  .contact__divider { width: 1px; background: var(--rule); margin-right: 12px; }
  .details { border-collapse: collapse; font-size: 10px; color: var(--text-soft); }
  .details td { padding: 1px 0; vertical-align: top; }
  .details__label { width: 62px; }
  .details__sep { width: 12px; }
  .details__value--strong { font-weight: 700; color: var(--text-white); }
</style>
</head>
<body>

  <section class="card card--back" aria-label="Card back">
    <div class="brand">
      <span class="brand__dot" aria-hidden="true"></span>
      <span class="brand__divider" aria-hidden="true"></span>
      <div>
        <div class="brand__name">Vortig Plumbing &amp; Gas</div>
        <div class="brand__tagline">Commercial Domestic &amp; Maintenance</div>
      </div>
    </div>
    <div class="web-band">
      <span class="web-band__url">www.vortigplumbingandgas.com</span>
    </div>
  </section>

  <section class="card card--front" aria-label="Card front">
    <div class="brand">
      <span class="brand__dot" aria-hidden="true"></span>
      <span class="brand__divider" aria-hidden="true"></span>
      <div>
        <div class="brand__name">Vortig Plumbing &amp; Gas</div>
        <div class="brand__tagline">Commercial Domestic &amp; Maintenance</div>
      </div>
    </div>
    <div class="contact">
      <div class="person">
        <div class="person__name">Name / Example</div>
        <div class="person__role">President / CEO</div>
      </div>
      <span class="contact__divider" aria-hidden="true"></span>
      <table class="details">
        <tr>
          <td class="details__label details__value--strong">Licence No.</td>
          <td class="details__sep details__value--strong">:</td>
          <td class="details__value--strong">617394K | ABN : 47215830962</td>
        </tr>
        <tr>
          <td class="details__label">Phone</td>
          <td class="details__sep">:</td>
          <td>0417382956</td>
        </tr>
        <tr>
          <td class="details__label">Email</td>
          <td class="details__sep">:</td>
          <td>vortigplumbingandgas@corvanet.com</td>
        </tr>
      </table>
    </div>
  </section>

</body>
</html>
```